We need a flyer where we promote a workshop to our members of the jewish community www.vbq-gemeinde.example . The workshop is calles "command in seven weeks presented by VBQ. We would like to see a flyer with the below text is used and also some pictures (attached). The flyer should come over as cool, fresh, innovative for a younger crowd so called young professionals (age 28-35).
TITLE.
"Command in Seven Weeks.
SUBTITLE.
Your systematic self-coaching roadmap to power and impact—and your future.”
TEXT.
Dr. Marcus L. Brandauer is the CEO Emeritus of Alpine Advisory Partners—he made an exit in 2013. He is the award-winning author of 8 books, including "Momentum-By-Design," "Speak Up or Fade" and "The Cantor and the Chairman.”
For the past 20 years he has taught leadership at Harwick University in New York and at KLB (Lindmoor University) to prepare future CEOs and other leaders in business, government , nonprofits and the military.
Now, in a process exclusively designed for VBQ’s next generation of emerging leaders, Marcus unpacks his leadership secrets in 3 action-packed labs—reduced to the max:
Lab 1. Command in Seven Weeks: The Summit Compass Model®. Self-Assessment. Self-Leadership: “The Lantern.” 5-Year Vision. 100-Day Catalytic Project.
Lab 2. Guiding Through Words. Relationship: Building Trust. Momentum-By-Design. Cockpit.
Lab 3. Debrief and Scale-Up. Sustainability. Action Tools.
Do you want to build your own future and a life you love? Do you want to jump-start that future and life over 100 days while learning a toolbox of leadership skills, networking with like-minded people—and even get some pizza? Then join us.
young professionals age 28-35

```html
<!DOCTYPE html>
<html lang="en">
<head>
<meta charset="utf-8">
<title>Command in Seven Weeks – VBQ Workshop Flyer</title>
<link rel="stylesheet" href="https://fonts.googleapis.com/css2?family=Bebas+Neue&family=Roboto:wght@400;700;900&display=swap">
<style>
:root{
  --blue:#1a8fdc;
  --blue-deep:#0b6fc0;
  --blue-navy:#0d4f8f;
  --sky:#6fcdf2;
  --pale:#e6eff8;
  --ink:#333a40;
  --name:#1461ad;
  --white:#ffffff;
  --frame:#7fd0f3;
}
*{margin:0;padding:0;box-sizing:border-box}
html,body{width:800px;height:1200px;overflow:hidden;background:#fff}
.flyer{position:relative;width:800px;height:1200px;overflow:hidden;background:var(--white);font-family:"Roboto",Arial,sans-serif;color:var(--ink)}
.abs{position:absolute}

/* hero */
.hero{left:0;top:0;width:800px;height:458px;background:linear-gradient(160deg,#2a9ee6 0%,var(--blue) 50%,#1583d2 100%)}
.hero-photo{left:0;top:0;width:800px;height:458px;clip-path:polygon(507px 0,800px 0,800px 458px,361px 458px);
  background:radial-gradient(ellipse at 60% 35%,#b04a50 0%,transparent 22%),linear-gradient(180deg,#1c1c2c 0%,#262a55 35%,#1f2f9a 70%,#17227a 100%)}
.hero-frame{left:0;top:0}
.brand{left:40px;top:44px;display:flex;align-items:center;gap:12px;color:var(--white);font-weight:400}
.brand-mark{font-size:72px;line-height:1;letter-spacing:-1px}
.brand-name{font-size:22px;line-height:1.15}
.title{left:36px;top:166px;font-family:"Bebas Neue","Arial Narrow",sans-serif;font-weight:400;color:var(--white);font-size:98px;line-height:1;letter-spacing:1px;white-space:nowrap}
.title-box{left:36px;top:256px;width:320px;height:88px;background:var(--white);border-radius:4px;display:flex;align-items:center;justify-content:center;
  font-family:"Bebas Neue","Arial Narrow",sans-serif;color:#3b3b3b;font-size:58px;line-height:1;padding-top:5px;white-space:nowrap}
.subtitle{left:38px;top:356px;width:360px;color:var(--white);font-weight:700;font-size:21.5px;line-height:1.08;white-space:nowrap}

/* bio */
.bio{left:0;top:458px;width:800px;height:192px;background:var(--pale)}
.book{left:64px;top:440px;width:112px;height:204px;background:linear-gradient(160deg,#c8211f 0%,#a1120f 60%,#2a1210 100%);box-shadow:4px 4px 8px rgba(0,0,0,.35)}
.bio-rule{left:215px;top:478px;width:2px;height:150px;background:#5aa9e0}
.bio-name{left:245px;top:482px;font-size:23px;color:var(--name);font-weight:400;letter-spacing:.2px}
.bio-text{left:245px;top:518px;width:500px;font-size:12.3px;line-height:1.3;color:#222}
.bio-text p+p{margin-top:12px}

/* intro */
.intro{left:36px;top:660px;width:740px;font-size:16.4px;font-weight:700;line-height:1.25;color:#404448}
.intro .accent{color:#1a7fd6}

/* labs */
.lab{top:746px;width:180px;height:180px}
.lab-circle{position:absolute;left:5px;top:14px;width:170px;height:170px;border-radius:50%;background:var(--white);box-shadow:0 2px 8px rgba(0,0,0,.18)}
.lab-pill{position:absolute;left:34px;top:0;width:112px;height:38px;border-radius:19px;background:linear-gradient(180deg,#29a9ee,#0f7fd0);
  display:flex;align-items:center;justify-content:center;gap:12px;color:var(--white);font-family:"Bebas Neue","Arial Narrow",sans-serif;font-size:31px;padding-top:3px}
.lab-num{width:29px;height:29px;border-radius:50%;background:var(--white);border:2px solid #0d5fa8;color:#12304e;font-family:"Roboto",Arial,sans-serif;font-weight:700;font-size:19px;display:flex;align-items:center;justify-content:center;margin-top:-3px}
.lab-body{position:absolute;left:24px;top:52px;width:140px;font-size:11.2px;line-height:1.22;color:#333}
.lab-head{font-size:12.6px;margin-bottom:6px;line-height:1.1}
.lab-list{list-style:none}
.lab-list li{position:relative;padding-left:13px;margin-bottom:2px}
.lab-list li::before{content:"";position:absolute;left:2px;top:4px;width:6px;height:6px;border-radius:50%;background:#2aa3e6}

/* quote */
.quote-photo{left:39px;top:928px;width:57px;height:68px;background:linear-gradient(180deg,#8fb2cf,#5c7387);border:1px solid #bbb}
.quote-rule{left:96px;height:1px;width:670px;background:#8a8a8a}
.quote{left:135px;top:940px;font-size:13.8px;line-height:1.3;color:#111}
.quote b{font-weight:700}

/* call */
.banner{left:0;top:1000px}
.banner-text{left:36px;top:1008px;font-size:16px;font-weight:400;color:#163149;letter-spacing:.1px;white-space:nowrap}
.call{left:36px;top:1041px;width:740px;font-size:13.8px;line-height:1.25;color:#222}
.call b{color:#1a7fd6;font-size:16px;font-weight:900}

/* footer */
.footer-shape{left:0;top:1090px}
.register{left:36px;top:1100px;font-family:"Bebas Neue","Arial Narrow",sans-serif;color:var(--sky);font-size:34px;letter-spacing:1px;line-height:1}
.email{left:36px;top:1140px;display:flex;align-items:center;gap:6px;color:var(--white);font-size:18px;font-weight:700}
.venue{left:382px;top:1092px;font-size:14.5px;font-weight:700;color:#222;line-height:1.05;font-style:normal}
.venue-org{color:#1a7fd6;font-weight:400;font-size:15px;margin-bottom:4px;margin-left:2px}
.venue-row{display:flex;gap:6px}
.contact{left:576px;top:1102px;font-size:13px;font-weight:700;color:#222;line-height:1}
.contact-row{display:flex;align-items:center;gap:8px;margin-bottom:14px;white-space:nowrap}
</style>
</head>
<body>
<main class="flyer">

  <section class="abs hero" aria-label="Header"></section>
  <div class="abs hero-photo" role="img" aria-label="Photo of the speaker on a conference stage in front of a large audience"></div>
  <svg class="abs hero-frame" width="800" height="1090" viewBox="0 0 800 1090" aria-hidden="true">
    <path d="M24 458 V34 Q24 26 32 26 H520" fill="none" stroke="#63c0f1" stroke-width="3" opacity=".7"/>
    <path d="M24 650 V1090" stroke="var(--frame)" stroke-width="3" fill="none"/>
    <path d="M775 650 V1090" stroke="var(--frame)" stroke-width="3" fill="none"/>
  </svg>

  <div class="abs brand">
    <span class="brand-mark">VBQ</span>
    <span class="brand-name">Vereinigte<br>Bürgergemeinde<br>Quellberg</span>
  </div>
  <h1 class="abs title">Command</h1>
  <div class="abs title-box">In Seven Weeks</div>
  <p class="abs subtitle">Your systematic self - coaching<br>roadmap to power and<br>impact - and your future</p>

  <section class="abs bio" aria-label="About the speaker"></section>
  <div class="abs book" role="img" aria-label="Cover of the book Command in Seven Weeks"></div>
  <div class="abs bio-rule"></div>
  <h2 class="abs bio-name">DR. MARCUS L. BRANDAUER</h2>
  <div class="abs bio-text">
    <p>Dr. Marcus L. Brandauer is the CEO Emeritus of Alpine Advisory Partners - he made an exit in 2013.</p>
    <p>It wasn't always like this. Marcus started out as a ski instructor in Davos, then worked as construction worker, actor, director, fundraiser and manager before becoming CEO.He is the award-winning author of 8 books, including "Momentum-By-Design," "Speak Up or Fade" and "The Cantor and the Chairman.</p>
  </div>

  <p class="abs intro">Now, in a process exclusively designed for VBQ’s next generation of emerging leaders, Marcus unpacks his leadership secrets in 3 action-packed labs - <span class="accent">reduced to the max:</span></p>

  <article class="abs lab" style="left:70px">
    <div class="lab-circle"></div>
    <div class="lab-pill">LAB <span class="lab-num">1</span></div>
    <div class="lab-body" style="left:22px;top:56px">
      <p class="lab-head">Command in Seven Weeks</p>
      <ul class="lab-list">
        <li>The Summit Compass Model®.</li>
        <li>Self-Assessment.</li>
        <li>100-Day Catalytic Project.</li>
      </ul>
    </div>
  </article>

  <article class="abs lab" style="left:303px">
    <div class="lab-circle"></div>
    <div class="lab-pill">LAB <span class="lab-num">2</span></div>
    <div class="lab-body" style="left:26px;top:48px">
      <p class="lab-head">Guiding Through Words</p>
      <ul class="lab-list">
        <li>Self-Leadership: “The Lantern.”</li>
        <li>Relationship: Building Trust. Momentum-By-Design. Cockpit.</li>
        <li>Vision: Futuring.</li>
        <li>Strategy: Roadmap.</li>
      </ul>
    </div>
  </article>

  <article class="abs lab" style="left:533px">
    <div class="lab-circle"></div>
    <div class="lab-pill">LAB <span class="lab-num">3</span></div>
    <div class="lab-body" style="left:22px;top:56px">
      <p class="lab-head">Debrief and Scale-Up</p>
      <ul class="lab-list">
        <li>Action Tools.</li>
        <li>Become Unstoppable: From Breakdown to Breakthrough.</li>
        <li>Rituals: Standardize Your Leadership.</li>
      </ul>
    </div>
  </article>

  <div class="abs quote-photo" role="img" aria-label="Portrait of the person quoted"></div>
  <div class="abs quote-rule" style="top:932px"></div>
  <blockquote class="abs quote">
    <b>"I wish I had had Brandauer's tools 35 years ago when I was starting out."</b><br>
    --K. Berger, President, Northfield Energy - Europe
  </blockquote>
  <div class="abs quote-rule" style="top:993px"></div>

  <svg class="abs banner" width="800" height="36" viewBox="0 0 800 36" aria-hidden="true">
    <polygon points="0,0 590,0 614,36 0,36" fill="var(--sky)"/>
    <polygon points="598,0 610,0 640,36 628,36" fill="var(--sky)"/>
  </svg>
  <p class="abs banner-text">DO YOU WANT TO BUILD YOUR OWN FUTURE AND A LIFE YOU LOVE?</p>
  <p class="abs call">Do you want to jump - start that future and life over 100 days while learning a toolbox of leadership skills, networking with like-minded people - and even get some pizza? <b>THEN JOIN US.</b></p>

  <svg class="abs footer-shape" width="800" height="110" viewBox="0 0 800 110" aria-hidden="true">
    <polygon points="0,0 322,0 368,110 0,110" fill="var(--blue-deep)"/>
    <polygon points="335,0 348,0 392,72 379,72" fill="var(--sky)"/>
    <polygon points="352,0 365,0 409,72 396,72" fill="var(--sky)"/>
    <path d="M368 108 H775 V60" fill="none" stroke="var(--frame)" stroke-width="3"/>
  </svg>
  <p class="abs register">REGISTER NOW ON</p>
  <p class="abs email">
    <svg width="18" height="13" viewBox="0 0 18 13" aria-hidden="true"><rect x="0.5" y="0.5" width="17" height="12" fill="none" stroke="#6fcdf2"/><path d="M1 1 L9 7 L17 1" fill="none" stroke="#6fcdf2"/></svg>
    info@vbq-gemeinde.example
  </p>

  <address class="abs venue">
    <p class="venue-org">VBQ</p>
    <div class="venue-row">
      <svg width="12" height="16" viewBox="0 0 12 16" aria-hidden="true"><path d="M6 0 C2.7 0 0 2.6 0 5.8 C0 10 6 16 6 16 C6 16 12 10 12 5.8 C12 2.6 9.3 0 6 0 Z" fill="#1a8fdc"/><circle cx="6" cy="5.8" r="2.3" fill="#fff"/></svg>
      <span>Gemeindezentrum<br>Lindenweg 12<br>8000 Quellberg</span>
    </div>
  </address>

  <div class="abs contact">
    <p class="contact-row">
      <svg width="17" height="17" viewBox="0 0 20 20" aria-hidden="true"><circle cx="10" cy="10" r="9" fill="none" stroke="#1a8fdc" stroke-width="2"/><ellipse cx="10" cy="10" rx="4" ry="9" fill="none" stroke="#1a8fdc" stroke-width="1.6"/><path d="M1 10 H19 M3 5 H17 M3 15 H17" stroke="#1a8fdc" stroke-width="1.4"/></svg>
      www.vbq-gemeinde.example
    </p>
    <p class="contact-row">
      <svg width="17" height="17" viewBox="0 0 20 20" aria-hidden="true"><path d="M4 1 L7.5 1 L9 6 L6.5 7.8 C7.6 10.3 9.7 12.4 12.2 13.5 L14 11 L19 12.5 L19 16 C19 17.7 17.7 19 16 19 C8 19 1 12 1 4 C1 2.3 2.3 1 4 1 Z" fill="#1a8fdc"/></svg>
      +41 44 555 01 23
    </p>
  </div>

</main>
</body>
</html>
```